Aesthetics Company Flyer (description of services)

We need a 5.5"x8.5" flyer describing the services we offer at velvet horizon aesthetics. We are an aesthetics company located in Conroe TX. Our products and services can be found at www.vhaesthetics-demo.com/services . We would like to see designs that are cohesive with our brand and website: https://www.vhaesthetics-demo.com/

```html
<!DOCTYPE html>
<html lang="en">
<head>
<meta charset="utf-8">
<title>Velvet Horizon Aesthetics – Our Services</title>
<link href="https://fonts.googleapis.com/css2?family=Poppins:wght@400;500;600;700;800&family=Pacifico&display=swap" rel="stylesheet">
<style>
  :root{
    --page:#ece8e3;
    --ink:#1d1b1f;
    --body:#2e2b31;
    --lavender:#c3a8d8;
    --lavender-soft:#efe6f6;
    --band:#b3a2c7;
    --peach:#e4aea6;
    --white:#ffffff;
  }
  *{box-sizing:border-box;margin:0;padding:0}
  html,body{width:1200px;height:1117px;overflow:hidden}
  body{background:var(--page);font-family:"Poppins",sans-serif;color:var(--ink);position:relative}
  .flyer{position:absolute;left:250px;top:18px;width:699px;height:1080px;background:var(--white);overflow:hidden}
  .wash{position:absolute;right:0;top:359px;width:440px;height:320px;
    background:radial-gradient(ellipse at 75% 35%,var(--lavender-soft) 0%,rgba(239,230,246,0) 70%)}
  .photo{position:absolute;top:0;height:359px}
  .photo-left{left:0;width:349px;background:linear-gradient(135deg,#c9967b 0%,#e2b9a0 40%,#6f8796 100%)}
  .photo-right{left:349px;width:350px;background:linear-gradient(135deg,#e9e6e4 0%,#d7cfcb 50%,#c49b91 100%)}
  .brand-seal{position:absolute;left:221px;top:40px;width:256px;height:256px;border-radius:50%;
    background:var(--white);border:4px solid var(--lavender);display:flex;align-items:center;justify-content:center;text-align:center}
  .brand-seal span{font-size:19px;font-weight:500;letter-spacing:3px;line-height:1.5;color:var(--ink);text-transform:uppercase}
  .headline-box{position:absolute;left:51px;top:292px;width:599px;height:143px;border:3px solid var(--lavender);
    border-radius:16px;background:var(--white);box-shadow:0 0 0 4px var(--white);text-align:center;padding-top:10px}
  .tagline{font-family:"Pacifico",cursive;color:var(--lavender);font-size:26px;line-height:1.15}
  .headline{font-weight:800;font-size:33px;line-height:1.05;letter-spacing:-.3px;margin-top:2px}
  .lotus{position:absolute;left:84px;top:388px;width:132px;height:89px;border-radius:50% 50% 45% 45%;
    background:radial-gradient(ellipse at 50% 45%,#f3d28e 0%,#fbf8f2 25%,#ece8e2 70%,rgba(255,255,255,0) 100%)}
  .services-title{position:absolute;left:0;width:699px;top:445px;text-align:center;font-weight:800;font-size:28px;letter-spacing:-.3px}
  .intro{position:absolute;left:49px;width:601px;top:485px;text-align:center;font-size:10.2px;line-height:14px;color:var(--body)}
  .band{position:absolute;left:0;top:917px;width:699px;height:163px;background:var(--band)}
  .card{position:absolute;left:31px;top:600px;width:637px;height:417px;background:var(--white);border-radius:0 0 18px 18px}
  .iv-bar{position:absolute;left:49px;top:546px;width:601px;height:30px;border-radius:15px;background:var(--peach);
    color:var(--white);font-weight:700;font-size:16px;text-align:center;line-height:30px}
  .iv-list{position:absolute;list-style:none;font-weight:700;font-size:14px;line-height:16px}
  .iv-list li{position:relative;padding-left:19px;margin-bottom:9.5px}
  .iv-list svg{position:absolute;left:0;top:2px;width:13px;height:12px}
  .col-1{left:75px;top:595px}
  .col-2{left:245px;top:595px}
  .col-3{left:456px;top:595px}
  .service{position:absolute;display:flex;gap:13px}
  .service .thumb{flex:0 0 89px;height:80px;border-radius:9px}
  .service h3{font-size:13px;font-weight:700;line-height:1.2;margin-bottom:3px;white-space:nowrap}
  .service p{font-size:9.5px;line-height:12px;color:var(--body)}
  .s-weight,.s-neuro,.s-filler{left:49px;width:290px}
  .s-fibrin,.s-derma,.s-peel{left:356px;width:296px}
  .s-weight,.s-fibrin{top:717px}
  .s-neuro,.s-derma{top:816px}
  .s-filler,.s-peel{top:915px}
  .thumb-weight{background:linear-gradient(135deg,#d9772f,#f2b37a 60%,#5d5a5c)}
  .thumb-fibrin{background:linear-gradient(135deg,#f4f1ee,#e3c7bb)}
  .thumb-neuro{background:linear-gradient(135deg,#ece9e7,#a9877b 60%,#3e3a3a)}
  .thumb-derma{background:linear-gradient(135deg,#2f3a56,#e8c1a9 55%,#d4a28c)}
  .thumb-filler{background:linear-gradient(135deg,#3fb7d4,#e6b29c 55%,#c98f7a)}
  .thumb-peel{background:linear-gradient(135deg,#2b2a2c,#e8c83a 50%,#8f8a86)}
  .contact{position:absolute;left:0;top:1041px;width:699px;display:flex;justify-content:center;align-items:center;gap:8px;
    color:var(--white);font-weight:700;font-size:14.5px}
  .contact .sep{font-weight:400;opacity:.9}
  .contact svg{width:12px;height:12px;vertical-align:-1px;margin-right:3px}
</style>
</head>
<body>
<main class="flyer">
  <div class="photo photo-left" role="img" aria-label="Portrait photo of a woman touching her glowing skin"></div>
  <div class="photo photo-right" role="img" aria-label="Photo of a smiling client relaxing with a drink during IV therapy"></div>
  <div class="wash"></div>

  <div class="brand-seal"><span>Velvet Horizon<br>Aesthetics</span></div>

  <div class="band"></div>
  <div class="card"></div>

  <section class="headline-box">
    <p class="tagline">Everyone is beautiful.</p>
    <h1 class="headline">WITH US, EVERYONE CAN FEEL<br>BEAUTIFUL TOO</h1>
  </section>
  <div class="lotus" role="img" aria-label="White lotus flower"></div>

  <h2 class="services-title">OUR SERVICES</h2>
  <p class="intro">At Velvet Horizon Aesthetics we offer a comprehensive list of aesthetic, skincare and weight loss services and IV hydration therapy. But before you embark on your journey with us, you must first book a consultation so we can assess and understand your needs and decide on the best option to address those needs.</p>

  <div class="iv-bar">IV HYDRATION</div>

  <svg width="0" height="0" style="position:absolute">
    <defs><symbol id="tick" viewBox="0 0 13 12"><path d="M1.5 6.5 L5 10 L11.5 2" fill="none" stroke="#c3a8d8" stroke-width="2.6" stroke-linecap="round" stroke-linejoin="round"/></symbol></defs>
  </svg>

  <ul class="iv-list col-1">
    <li><svg><use href="#tick"/></svg>Quench Hydrator</li>
    <li><svg><use href="#tick"/></svg>Glutathione</li>
    <li><svg><use href="#tick"/></svg>Vitamin Cocktail</li>
    <li><svg><use href="#tick"/></svg>Hangover</li>
  </ul>
  <ul class="iv-list col-2">
    <li><svg><use href="#tick"/></svg>Post Workout Recovery</li>
    <li><svg><use href="#tick"/></svg>Migraine Rescue</li>
    <li><svg><use href="#tick"/></svg>Immunity Booster</li>
  </ul>
  <ul class="iv-list col-3">
    <li><svg><use href="#tick"/></svg>Velvet Glow</li>
    <li><svg><use href="#tick"/></svg>Peak<br>Athletic Performance</li>
    <li><svg><use href="#tick"/></svg>NAD+</li>
  </ul>

  <article class="service s-weight">
    <div class="thumb thumb-weight" role="img" aria-label="Photo of a weight loss injection pen"></div>
    <div><h3>Weightloss</h3><p>Semaglutide stimulates insulin to be released from the pancreas in an effort to slow down gastric emptying and inhibits inappropriate release of sugars after we eat.</p></div>
  </article>
  <article class="service s-fibrin">
    <div class="thumb thumb-fibrin" role="img" aria-label="Photo of a facial treatment"></div>
    <div><h3>Fibrin Growth Factor (FGF)</h3><p>Fibrin Growth Factor (FGF) facial treatment enhances skin rejuvenation, scar and wound rejuvenation, and hair restoration by injecting plasma rich fibrin into the face.</p></div>
  </article>
  <article class="service s-neuro">
    <div class="thumb thumb-neuro" role="img" aria-label="Photo of a wrinkle relaxer injection"></div>
    <div><h3>Neurotoxin (Wrinkle Relaxer)</h3><p>Neurotoxin injections lessens facial lines that can give you a tired appearance. These lines are produced by repeated muscle contractions most noticeable on the forehead, between the eyebrows and around the eyes.</p></div>
  </article>
  <article class="service s-derma">
    <div class="thumb thumb-derma" role="img" aria-label="Photo of a microneedling treatment"></div>
    <div><h3>DermaDot®</h3><p>DermaDot® is a microneedling treatment that generates the skin's self-repair mechanism and activates collagen and elastin production.</p></div>
  </article>
  <article class="service s-filler">
    <div class="thumb thumb-filler" role="img" aria-label="Photo of a dermal filler treatment"></div>
    <div><h3>Dermal Fillers</h3><p>Dermal filler treatments plump up smile and frown lines, thin lips, and decrease cheek wrinkles and chin folds with FDA-approved volumizing hyaluronic acid, thus allow skin to restore fullness from the inside out.</p></div>
  </article>
  <article class="service s-peel">
    <div class="thumb thumb-peel" role="img" aria-label="Photo of a chemical peel being applied"></div>
    <div><h3>Chemical Peels</h3><p>Chemical Peels improve skin<br>texture correcting pigmentation<br>concerns, sun damage,<br>and scarring.</p></div>
  </article>

  <footer class="contact">
    <span><svg viewBox="0 0 12 12"><circle cx="6" cy="6" r="6" fill="#fff"/><path d="M3.6 3.2c.4-.4.8-.3 1 .1l.5.9c.2.3.1.6-.2.8l-.3.2c.3.7.9 1.3 1.6 1.6l.2-.3c.2-.3.5-.4.8-.2l.9.5c.4.2.5.6.1 1-.6.6-1.4.6-2.3.1C4.8 7.3 4 6.5 3.5 5.5c-.5-.9-.5-1.7.1-2.3z" fill="#b3a2c7"/></svg>936 555 0142</span>
    <span class="sep">|</span>
    <span><svg viewBox="0 0 12 12"><circle cx="6" cy="6" r="6" fill="#fff"/><rect x="3" y="4" width="6" height="4.2" rx=".6" fill="none" stroke="#b3a2c7" stroke-width=".9"/><path d="M3.2 4.3 6 6.4l2.8-2.1" fill="none" stroke="#b3a2c7" stroke-width=".9"/></svg>hello@vhaesthetics-demo.com</span>
    <span class="sep">|</span>
    <span><svg viewBox="0 0 12 12"><circle cx="6" cy="6" r="6" fill="#fff"/><circle cx="6" cy="6" r="3.3" fill="none" stroke="#b3a2c7" stroke-width=".8"/><path d="M2.7 6h6.6M6 2.7c-1.6 2-1.6 4.6 0 6.6M6 2.7c1.6 2 1.6 4.6 0 6.6" fill="none" stroke="#b3a2c7" stroke-width=".8"/></svg>www.vhaesthetics-demo.com</span>
  </footer>
</main>
</body>
</html>
```